Corvane Networks web design

Corvane is an Internet Service Provider bringing high-speed service to homes and businesses. Our principal market target is rural areas of West Michigan, but we intend to expand rapidly. We need a website to market our services, facilitate online ordering, customer support and communicate with our customers.

I will upload a draft outline of the content we hope to include in the website.

We compete directly with Halberd Communications, Lumetra, Dravix and Kelwick communications to bring Internet service to homes and businesses in our coverage area.

Our primary values include:

1. Unlike our competitors, we do not require long term contractors or service bundles; There are no termination fees, for example. All services are sold on a recurring 1-month agreement term.
2. Unlike other wireless (mobile) providers, we do not limit downloads or uploads with bit/byte buckets
3. We provide service to areas ignored by the larger carriers - Rural areas in Michigan that lack options for broadband are prime targets for Corvane to cover.
4. Unlike other wireless ISP's, we utilize licensed FCC spectrum. We do not use unlicensed/free frequencies, providing us an advantage for reliability and stability.
Updates

So many wonderful designs, thank you very much for all your hard work. We are evaluating all our favorite designs and plan to make a selection in the next 2 days. I will be in touch with you to request revisions if necessary or further refinements.  Thank you again for your efforts on this project.

Target Market(s)

Our target market is home Internet users. however, that does not mean that our users are "high tech" oriented - they are just normal mom's and pop's who buy Internet for home use. The site should be easy to navigate and communicate our message of speed, value, reliability and facilitate simple product ordering.

Industry/Entity Type

Internet

Requirements
Must have
• Our phone number should be prominently displayed 1-844-7NU-LINK
• Our logo is uploaded in the attachments.
• Design for desktop and mobile devices.
Nice to have
• The most modern of web design trends. Such as a design that facilitates parallax scrolling effects rather than lots of individual pages.
• Stock artwork communicating our values of speed and reliability.

```html
<!DOCTYPE html>
<html lang="en">
<head>
<meta charset="utf-8">
<title>Corvane Networks</title>
<link href="https://fonts.googleapis.com/css2?family=Oswald:wght@400;500;600&family=Roboto+Condensed:wght@300;400;700&family=Open+Sans:wght@400;600;700&family=Montserrat:wght@400;600;700&display=swap" rel="stylesheet">
<style>
:root{
  --orange:#f7930e;
  --orange-soft:#fdd284;
  --teal:#2aa3b6;
  --teal-light:#62c3d1;
  --mint:#2fd5c0;
  --ink:#333;
  --grey:#777;
  --line:#e6e6e6;
  --footer:#323232;
  --footer-deep:#1b1b1b;
  --blue:#2aa3e0;
}
*{margin:0;padding:0;box-sizing:border-box}
html,body{width:787px;height:1200px;overflow:hidden;background:#fff}
body{position:relative;font-family:'Open Sans',sans-serif;color:var(--ink)}
.abs{position:absolute}
.topbar{left:0;top:0;width:787px;height:24px;background:#474747;color:#eee;font-size:8px;font-family:'Open Sans',sans-serif}
.topbar .connect{left:88px;top:7px}
.topbar .sq{top:6px;width:10px;height:10px;background:#666}
.topbar .call{right:93px;top:6px;font-size:8px}
.topbar .call b{font-size:10px;font-weight:600;margin-left:3px}
.header{left:0;top:24px;width:787px;height:58px;background:#fff}
.logo{left:88px;top:18px;font-family:'Montserrat',sans-serif;font-weight:700;font-size:20px;color:var(--orange);letter-spacing:1px}
.nav-item{top:12px;text-align:center;font-family:'Roboto Condensed',sans-serif;font-size:9px;color:#222;border-bottom:1px solid #ccc;padding-bottom:3px}
.nav-item svg{display:block;margin:0 auto 4px}
.nav-item.active{color:var(--orange)}
.hero{left:0;top:82px;width:787px;height:316px;background:linear-gradient(120deg,#59bccb 0%,#2f9fb2 55%,#2391a6 100%)}
.hero h1{left:92px;top:38px;font-family:'Oswald',sans-serif;font-weight:600;font-size:27px;line-height:28px;color:#fff}
.hero p{left:92px;top:104px;width:320px;font-family:'Roboto Condensed',sans-serif;font-weight:300;font-size:12px;line-height:18px;color:#fff}
.hero ul{left:92px;top:149px;list-style:none;font-family:'Roboto Condensed',sans-serif;font-weight:300;font-size:12px;color:#fff}
.hero li{height:21px;display:flex;align-items:center}
.hero li svg{margin-right:5px}
.hero-photo{left:395px;top:38px;width:315px;height:278px;border-radius:120px 120px 0 0;background:linear-gradient(180deg,#5b7fa8,#3e5f8b)}
.arrow{top:216px;width:23px;height:28px;background:#fff;border:1px solid #ddd;display:flex;align-items:center;justify-content:center}
.plans-title{left:0;top:420px;width:787px;text-align:center;font-family:'Oswald',sans-serif;font-weight:500;font-size:27px;color:#555}
.plan{background:#fff;border:1px solid var(--line)}
.plan-head{position:absolute;left:0;top:0;width:100%;color:#fff;text-align:center;font-family:'Montserrat',sans-serif}
.plan-head .name{font-size:12px;margin-top:13px}
.plan-head .price{font-size:39px;line-height:40px;font-weight:400}
.plan-head .price sup{font-size:15px;vertical-align:16px}
.plan-head .price small{font-size:7px;font-weight:700}
.stat{position:absolute;text-align:center;font-family:'Montserrat',sans-serif}
.stat b{display:block;font-size:12px;font-weight:700;color:#222}
.stat span{font-size:7px;color:#444}
.divider{position:absolute;width:1px;height:12px;background:#ccc}
.buy{position:absolute;height:26px;color:#fff;font-family:'Montserrat',sans-serif;font-weight:700;font-size:13px;display:flex;align-items:center;justify-content:center;box-shadow:0 2px 3px rgba(0,0,0,.15)}
.sec-title{top:704px;font-family:'Roboto Condensed',sans-serif;font-weight:700;font-size:12px;color:#333}
.post-icon{width:30px;height:30px;display:flex;align-items:center;justify-content:center}
.post-title{width:135px;font-size:8px;line-height:11px;color:#333}
.post-date{width:28px;text-align:center;font-family:'Roboto Condensed',sans-serif;font-style:italic;color:#444;font-size:15px;line-height:15px}
.post-date small{display:block;font-size:6px}
.post-body{width:135px;font-size:7.5px;line-height:11px;color:#777}
.more{font-size:8.5px;color:var(--orange)}
.sep{height:3px;border-top:1px dotted #ccc;border-bottom:1px dotted #ccc}
.tweet-dot{width:22px;height:22px;border-radius:50%;background:var(--blue)}
.tweet{width:140px;font-size:7.5px;line-height:12px;color:#555}
.tweet a{color:var(--blue);text-decoration:none}
.tweet em{font-style:normal;color:#bbb;display:block}
.staff-photo{width:67px;height:54px;border:1px solid #ddd;background:linear-gradient(135deg,#dfe5ea,#b9c4cc)}
.staff-name{font-family:'Montserrat',sans-serif;font-size:8.5px;color:#222}
.staff-desc{width:115px;font-size:7px;line-height:11px;color:#888}
.footer{left:0;top:964px;width:787px;height:194px;background:var(--footer)}
.foot-title{top:20px;font-family:'Open Sans',sans-serif;font-weight:600;font-size:11px;color:#fff}
.foot-text{font-size:7.5px;line-height:13px;color:#aaa}
.foot-rule{top:20px;width:1px;height:170px;background:#444}
.rb-thumb{width:31px;height:31px;background:linear-gradient(135deg,#c9c2b4,#6f6a62)}
.rb-title{font-size:8px;line-height:11px;color:#bbb;width:70px}
.rb-date{font-size:6px;color:#777}
.soc{width:22px;height:22px;border-radius:50%;background:#5a5a5a}
.chat{left:594px;top:111px;width:97px;height:33px;background:#444;color:#fff;font-family:'Open Sans',sans-serif;font-weight:600;font-size:11px;display:flex;align-items:center;justify-content:center;gap:7px}
.bottom{left:0;top:1158px;width:787px;height:42px;background:var(--footer-deep);color:#ddd;font-size:7.5px;text-align:center;line-height:42px}
</style>
</head>
<body>

<div class="abs topbar">
  <span class="abs connect">Connect With Us:</span>
  <span class="abs sq" style="left:150px"></span><span class="abs sq" style="left:163px"></span><span class="abs sq" style="left:176px"></span><span class="abs sq" style="left:189px"></span><span class="abs sq" style="left:202px"></span><span class="abs sq" style="left:215px"></span><span class="abs sq" style="left:228px"></span>
  <span class="abs call">Call Us: <b>1-844-7NU-LINK</b></span>
</div>

<header class="abs header">
  <div class="abs logo">CORVANE <span style="display:block;font-size:9px;font-weight:400;letter-spacing:5px;color:#333;margin-top:-4px">NETWORKS</span></div>
  <nav>
    <div class="abs nav-item active" style="left:404px;width:28px"><svg width="9" height="9" viewBox="0 0 10 10"><path d="M5 1L1 5h1.5v4h2V6.5h1V9h2V5H9z" fill="#333"/></svg>HOME</div>
    <div class="abs nav-item" style="left:452px;width:42px"><svg width="10" height="9" viewBox="0 0 10 9"><rect x="1" y="1" width="8" height="5" fill="#555"/><rect x="3" y="7" width="4" height="1" fill="#555"/></svg>SERVICES</div>
    <div class="abs nav-item" style="left:517px;width:40px"><svg width="8" height="9" viewBox="0 0 8 9"><rect x="1" y="1" width="6" height="7" fill="none" stroke="#555"/><line x1="2" y1="4" x2="6" y2="4" stroke="#555"/></svg>WIRELESS</div>
    <div class="abs nav-item" style="left:580px;width:44px"><svg width="9" height="9" viewBox="0 0 10 10"><path d="M2 6V5a3 3 0 016 0v1" fill="none" stroke="#555" stroke-width="1.3"/><rect x="1.5" y="5.5" width="2" height="3" fill="#555"/><rect x="6.5" y="5.5" width="2" height="3" fill="#555"/></svg>COVERAGE</div>
    <div class="abs nav-item" style="left:646px;width:52px"><svg width="7" height="9" viewBox="0 0 7 10"><path d="M3.5 0.5a3 3 0 013 3c0 2-3 6-3 6s-3-4-3-6a3 3 0 013-3z" fill="#555"/></svg>CONTACT US</div>
  </nav>
</header>

<section class="abs hero">
  <h1 class="abs">West Michigan’s Best<br>Internet Service</h1>
  <p class="abs">Corvane Networks is a Michigan-based company providing high-speed Internet services to West Michigan homes and businesses.</p>
  <ul class="abs">
    <li><svg width="9" height="9" viewBox="0 0 10 10"><circle cx="5" cy="5" r="5" fill="#fff"/><path d="M2.7 5.2l1.6 1.6 3-3.3" fill="none" stroke="#2f9fb2" stroke-width="1.4"/></svg>100% Satisfaction Guaranteed.</li>
    <li><svg width="9" height="9" viewBox="0 0 10 10"><circle cx="5" cy="5" r="5" fill="#fff"/><path d="M2.7 5.2l1.6 1.6 3-3.3" fill="none" stroke="#2f9fb2" stroke-width="1.4"/></svg>Honest Pricing, No Hidden Fees</li>
    <li><svg width="9" height="9" viewBox="0 0 10 10"><circle cx="5" cy="5" r="5" fill="#fff"/><path d="M2.7 5.2l1.6 1.6 3-3.3" fill="none" stroke="#2f9fb2" stroke-width="1.4"/></svg>No Long Term Contracts.</li>
    <li><svg width="9" height="9" viewBox="0 0 10 10"><circle cx="5" cy="5" r="5" fill="#fff"/><path d="M2.7 5.2l1.6 1.6 3-3.3" fill="none" stroke="#2f9fb2" stroke-width="1.4"/></svg>No Phone Line or Cable TV required.</li>
    <li><svg width="9" height="9" viewBox="0 0 10 10"><circle cx="5" cy="5" r="5" fill="#fff"/><path d="M2.7 5.2l1.6 1.6 3-3.3" fill="none" stroke="#2f9fb2" stroke-width="1.4"/></svg>Fast, Superior Performance for your home and business.</li>
    <li><svg width="9" height="9" viewBox="0 0 10 10"><circle cx="5" cy="5" r="5" fill="#fff"/><path d="M2.7 5.2l1.6 1.6 3-3.3" fill="none" stroke="#2f9fb2" stroke-width="1.4"/></svg>Interference-Free FCC Licensed 4G Coverage..</li>
  </ul>
  <div class="abs hero-photo" role="img" aria-label="Smiling man in glasses and blue shirt holding an open laptop showing network cables"></div>
  <div class="abs arrow" style="left:0"><svg width="6" height="10"><path d="M5 1L1 5l4 4" fill="none" stroke="#999"/></svg></div>
  <div class="abs arrow" style="left:764px"><svg width="6" height="10"><path d="M1 1l4 4-4 4" fill="none" stroke="#999"/></svg></div>
</section>

<h2 class="abs plans-title">Pick the Plan that is right for you</h2>

<div class="abs plan" style="left:93px;top:489px;width:191px;height:173px">
  <div class="plan-head" style="height:81px;background:linear-gradient(120deg,#36dcc4,#20c4b7)"><div class="name">STARTER</div><div class="price"><sup>$</sup>99<small>/ MO</small></div></div>
  <div class="stat" style="left:22px;top:93px;width:60px"><b>5,000</b><span>CONTACTS</span></div>
  <div class="divider" style="left:95px;top:98px"></div>
  <div class="stat" style="left:108px;top:93px;width:70px"><b>Unlimited</b><span>EMAILS SENT</span></div>
  <div class="buy" style="left:15px;top:131px;width:159px;background:var(--orange-soft)">Buy</div>
</div>
<div class="abs plan" style="left:506px;top:489px;width:191px;height:173px">
  <div class="plan-head" style="height:81px;background:linear-gradient(100deg,#22c3c2,#87b0e6)"><div class="name">PREMIUM</div><div class="price"><sup>$</sup>299<small>/ MO</small></div></div>
  <div class="stat" style="left:15px;top:93px;width:66px"><b>100,000</b><span>CONTACTS</span></div>
  <div class="divider" style="left:95px;top:98px"></div>
  <div class="stat" style="left:108px;top:93px;width:70px"><b>Unlimited</b><span>EMAILS SENT</span></div>
  <div class="buy" style="left:15px;top:131px;width:159px;background:var(--orange-soft)">Buy</div>
</div>
<div class="abs plan" style="left:284px;top:477px;width:221px;height:198px;box-shadow:0 0 4px rgba(0,0,0,.08)">
  <div class="plan-head" style="height:93px;background:linear-gradient(120deg,#1fcab9,#0fb1c0)"><div class="name" style="margin-top:25px">STANDARD</div><div class="price"><sup>$</sup>199<small>/ MO</small></div></div>
  <div class="stat" style="left:25px;top:105px;width:62px"><b>25,000</b><span>CONTACTS</span></div>
  <div class="divider" style="left:110px;top:110px"></div>
  <div class="stat" style="left:130px;top:105px;width:70px"><b>Unlimited</b><span>EMAILS SENT</span></div>
  <div class="buy" style="left:27px;top:143px;width:166px;background:var(--orange)">Buy</div>
</div>

<h3 class="abs sec-title" style="left:97px">COMPANY’S BLOG</h3>
<h3 class="abs sec-title" style="left:300px">LATEST TWEETS</h3>
<h3 class="abs sec-title" style="left:495px">OUR STAFF</h3>

<div class="abs post-icon" style="left:98px;top:735px;background:#e35a16"><svg width="14" height="12" viewBox="0 0 14 12"><path d="M2 9V7a5 5 0 0110 0v2" fill="none" stroke="#fff" stroke-width="1.6"/><rect x="1" y="7" width="3" height="4" fill="#fff"/><rect x="10" y="7" width="3" height="4" fill="#fff"/></svg></div>
<div class="abs post-title" style="left:148px;top:740px">Contrary to popula belieflorem the Ipsum is simply</div>
<div class="abs post-date" style="left:101px;top:772px">31<small>01,13</small></div>
<div class="abs post-body" style="left:148px;top:770px">Lorem Ipsum is dummy text the printing and typesetting instry. Ipsum has been.Lorem Ipsis sly</div>
<div class="abs more" style="left:149px;top:807px">View More</div>
<div class="abs sep" style="left:98px;top:832px;width:186px"></div>
<div class="abs post-icon" style="left:98px;top:846px;background:#5aa9d6"><svg width="14" height="12" viewBox="0 0 14 12"><rect x="1" y="1" width="12" height="10" fill="none" stroke="#fff" stroke-width="1.3"/><path d="M2 10l4-4 3 3 2-2 2 3" fill="#fff"/></svg></div>
<div class="abs post-title" style="left:148px;top:850px">Contrary to popula belieflorem the Ipsum is simply</div>
<div class="abs post-date" style="left:101px;top:882px">31<small>01,13</small></div>
<div class="abs post-body" style="left:148px;top:880px">Lorem Ipsum is dummy text the printing and typesetting instry. Ipsum has been.Lorem Ipsis sly</div>
<div class="abs more" style="left:149px;top:918px">View More</div>

<div class="abs tweet-dot" style="left:310px;top:737px"></div>
<div class="abs tweet" style="left:343px;top:734px"><a>@nova_reid</a> Lorem Ipsum is the dummy text the printing typeset-ting instry Ipsum is has been.Lorem<em>3 days ago</em></div>
<div class="abs sep" style="left:300px;top:789px;width:178px"></div>
<div class="abs tweet-dot" style="left:310px;top:805px"></div>
<div class="abs tweet" style="left:343px;top:802px"><a>@nova_reid</a> Lorem Ipsum is the dummy text the printing typeset-ting instry Ipsum is has been.Lorem<em>3 days ago</em></div>
<div class="abs sep" style="left:300px;top:857px;width:178px"></div>
<div class="abs tweet-dot" style="left:310px;top:873px"></div>
<div class="abs tweet" style="left:343px;top:870px"><a>@nova_reid</a> Lorem Ipsum is the dummy text the printing typeset-ting instry Ipsum is has been.Lorem<em>3 days ago</em></div>
<div class="abs more" style="left:314px;top:917px">View All</div>

<div class="abs staff-photo" style="left:498px;top:737px" role="img" aria-label="Staff portrait"></div>
<div class="abs staff-name" style="left:574px;top:739px">LOREM IPSUM</div>
<div class="abs staff-desc" style="left:574px;top:755px">Lorem Ipsum Dolor sit amet and typesetting industry and ipsum and ending etc</div>
<div class="abs staff-photo" style="left:498px;top:800px" role="img" aria-label="Staff portrait"></div>
<div class="abs staff-name" style="left:574px;top:802px">LOREM IPSUM</div>
<div class="abs staff-desc" style="left:574px;top:818px">Lorem Ipsum Dolor sit amet and typesetting industry and ipsum and ending etc</div>
<div class="abs staff-photo" style="left:498px;top:862px" role="img" aria-label="Staff portrait"></div>
<div class="abs staff-name" style="left:574px;top:865px">LOREM IPSUM</div>
<div class="abs staff-desc" style="left:574px;top:881px">Lorem Ipsum Dolor sit amet and typesetting industry and ipsum and ending etc</div>

<footer class="abs footer">
  <h4 class="abs foot-title" style="left:94px">ABOUT US</h4>
  <p class="abs foot-text" style="left:93px;top:44px;width:100px">All the you need to be sure there isn't anything embarr assing hiddens the middle text lorempsum generators on the Internet tend to the repeat predefined chunks as necessary, making this the first true generator on the internet versions have evolved over the years.</p>
  <div class="abs foot-rule" style="left:204px"></div>
  <h4 class="abs foot-title" style="left:218px">RECENT BLOGS</h4>
  <div class="abs rb-thumb" style="left:218px;top:47px" role="img" aria-label="Blog thumbnail of a living room"></div>
  <div class="abs rb-title" style="left:258px;top:48px">Internet repeat define chunks<div class="rb-date">June 27, 2013</div></div>
  <div class="abs rb-thumb" style="left:218px;top:96px" role="img" aria-label="Blog thumbnail of a living room"></div>
  <div class="abs rb-title" style="left:258px;top:97px">Majority have super ateration<div class="rb-date">June 26, 2013</div></div>
  <div class="abs rb-thumb" style="left:218px;top:145px" role="img" aria-label="Blog thumbnail of an office"></div>
  <div class="abs rb-title" style="left:258px;top:146px">Many desktop push packages<div class="rb-date">June 25, 2013</div></div>
  <div class="abs foot-rule" style="left:329px"></div>
  <h4 class="abs foot-title" style="left:343px">SUPPORT &amp; HELP</h4>
  <p class="abs foot-text" style="left:343px;top:46px;line-height:13.6px">Service Plans<br>coverage map<br>who is corvane<br>company blog<br>cusomer support<br>account management</p>
  <div class="abs foot-rule" style="left:454px"></div>
  <h4 class="abs foot-title" style="left:468px">CONTACT US</h4>
  <p class="abs foot-text" style="left:469px;top:47px;line-height:13.6px">Corvane Networks, LLC<br>118 Orchard lane<br>grand haven, mi 49417</p>
  <p class="abs foot-text" style="left:469px;top:92px;font-size:8.5px">616-555-0142</p>
  <div class="abs foot-rule" style="left:579px"></div>
  <h4 class="abs foot-title" style="left:594px">FALLOW US</h4>
  <span class="abs soc" style="left:594px;top:43px"></span><span class="abs soc" style="left:619px;top:43px"></span><span class="abs soc" style="left:644px;top:43px"></span><span class="abs soc" style="left:669px;top:43px"></span>
  <span class="abs soc" style="left:594px;top:71px"></span><span class="abs soc" style="left:619px;top:71px"></span><span class="abs soc" style="left:644px;top:71px"></span><span class="abs soc" style="left:669px;top:71px"></span>
  <div class="abs chat"><svg width="18" height="14" viewBox="0 0 18 14"><ellipse cx="7" cy="6" rx="6.5" ry="4.5" fill="#bbb"/><path d="M3 9l-1 4 4-3z" fill="#bbb"/><ellipse cx="12" cy="8" rx="5" ry="3.5" fill="#888"/></svg>LIVE CHAT</div>
</footer>
<div class="abs bottom">©COPYRIGHT 2014. ALL RIGHTS RESERVED</div>

</body>
</html>
```